Flyer required for podiatry clinic

DL Size please.
Wanting a design for a mail box flyer for the local area. Wanting to increase our customer base. The information on the attached word document needs to be included.
If stock photos are able to be fit in that would be appreciated
We cater from young children to the elderly so should be suitable for all.

Colors

Designer to choose colors to be used in the design.

```html
<!DOCTYPE html>
<html lang="en">
<head>
<meta charset="utf-8">
<title>Stride Podiatry – DL Flyer</title>
<link rel="stylesheet" href="https://fonts.googleapis.com/css2?family=PT+Sans:wght@400;700&display=swap">
<style>
  :root{
    --backdrop:#8a8a8a;
    --teal-dark:#235a6d;
    --teal-logo:#1f7d99;
    --cyan:#29b0d8;
    --green:#99b63c;
    --green-tag:#8fb43a;
    --white:#ffffff;
    --sky:#cfe3ea;
    --sand:#e9c9a0;
    --sea:#8fa6a8;
  }
  html,body{margin:0;padding:0;width:1200px;height:1200px;overflow:hidden;background:var(--backdrop);}
  body{font-family:"PT Sans",sans-serif;}
  .flyer{position:absolute;left:345px;top:75px;width:510px;height:1050px;overflow:hidden;background:var(--teal-dark);color:var(--white);}
  .hero-photo{position:absolute;left:0;top:0;width:510px;height:700px;
    background:linear-gradient(180deg,var(--sky) 0%,#f0dcc0 22%,var(--sand) 36%,#d8b48c 46%,var(--sea) 62%,#52808c 80%,var(--teal-dark) 100%);}
  .brand{position:absolute;left:0;top:40px;width:510px;text-align:center;font-weight:700;font-size:54px;line-height:52px;color:var(--teal-logo);margin:0;}
  .services{position:absolute;left:22px;top:500px;margin:0;padding:0;list-style:none;font-weight:700;font-size:24px;line-height:25.8px;}
  .services li::before{content:"• ";}
  .billing{position:absolute;left:0;top:722px;width:510px;height:84px;background:var(--cyan);text-align:center;font-weight:700;font-size:18.5px;line-height:25px;padding-top:10px;box-sizing:border-box;margin:0;}
  .locations-tag{position:absolute;left:143px;top:793px;width:214px;height:29px;background:var(--green-tag);text-align:center;font-weight:700;font-size:21px;line-height:29px;margin:0;}
  .locations{position:absolute;left:0;top:834px;width:510px;display:flex;}
  .location{flex:1;text-align:center;}
  .location + .location{border-left:1px solid var(--green-tag);}
  .location-name{font-weight:700;font-size:14px;line-height:19px;margin:0;}
  .location-address{font-weight:700;font-size:11px;line-height:15px;margin:2px 0 2px;}
  .location-phone{font-weight:700;font-size:18px;line-height:20px;margin:0;}
  .footer-wave{position:absolute;left:0;top:880px;}
  .footer{position:absolute;left:0;top:978px;width:510px;text-align:center;}
  .website{font-weight:700;font-size:12.5px;margin:0;display:flex;justify-content:center;align-items:center;gap:6px;}
  .staff{font-size:14.5px;margin:8px 0 0;}
</style>
</head>
<body>
<main class="flyer">
  <div class="hero-photo" role="img" aria-label="Stock photo: family playing barefoot on a beach at sunset, father lifting a child in the air"></div>
  <h1 class="brand">Stride<br>Podiatry</h1>

  <ul class="services">
    <li>Heel Pain- Spurs and Plantar Fasciitis</li>
    <li>Orthotics</li>
    <li>Fungal Nail Infections (Laser treatment)</li>
    <li>Diabetes Foot Assessments</li>
    <li>Foot and ankle pain</li>
    <li>Flat Feet- Both adults and children</li>
    <li>Ingrown nails</li>
    <li>Corns/Callus</li>
  </ul>

  <p class="billing">BULK BILLING for GP EPC/ Care plans , DVA<br>Card Holders.HealthClaim and card payments available</p>
  <p class="locations-tag">3 Handy locations</p>

  <section class="locations">
    <div class="location">
      <p class="location-name">Bayside Private<br>Medical Centre:</p>
      <p class="location-address">Level 1, 418 Marlow<br>Lane Eastvale</p>
      <p class="location-phone">Ph: 9000 1234</p>
    </div>
    <div class="location">
      <p class="location-name">Riverside<br>Rehabilitation:</p>
      <p class="location-address">54 Harlow Street<br>Eastvale</p>
      <p class="location-phone">Ph: 9000 5678</p>
    </div>
    <div class="location">
      <p class="location-name">Family Wellness<br>Hub:</p>
      <p class="location-address">412 Marlow Lane<br>Eastvale</p>
      <p class="location-phone">Ph: 9000 2468</p>
    </div>
  </section>

  <svg class="footer-wave" width="510" height="170" viewBox="0 0 510 170" aria-hidden="true">
    <path d="M0 82 C260 80 440 70 510 42 L510 170 L0 170 Z" fill="var(--green)"/>
    <path d="M0 80 C260 78 440 68 510 40" fill="none" stroke="var(--white)" stroke-width="3"/>
  </svg>

  <footer class="footer">
    <p class="website">
      <svg width="12" height="12" viewBox="0 0 12 12" aria-hidden="true"><g fill="none" stroke="#fff" stroke-width="1"><circle cx="6" cy="6" r="5"/><ellipse cx="6" cy="6" rx="2.2" ry="5"/><path d="M1 6h10"/></g></svg>
      www.stride-podiatry.example
    </p>
    <p class="staff">Podiatrist Daniel Ashworth, Maria Selby, Joanne Patel</p>
  </footer>
</main>
</body>
</html>
```